Visual design for database driven web application

Need a clean, professional looking visual design for a web application.

PLUMB is the new standardized K-12 school testing program for the state of Texas. We are building an application named PLUMB-Finder (clever, yeah?) that will allow teachers, school administrators, and others to EASILY sort through millions of records of student data and print or export reports showing just the information they need about their students.

The state currently doesn't provide a user-friendly way to do this. They provide a "data dump" spreadsheet that school administrators and teachers must figure out how to manipulate to get the data they need. We are building a Web-based tool that will make it super simple and easy for our users to get the data they need in a format that works for them.

I've created a basic wireframe of the main application screen in Wirella Kit Plus. I need you to "skin" the wireframe to make it look good. Your mockup will set the tone for branding and visual design throughout the site.

See the attached screenshots. There are a few variations of the screen that include dynamic panels that open & close. Start by designing just the main screen and if you have time, do one or two of the panels. Thanks!
Updates

Target Market(s)

K-12 education professionals (teachers, administrators) in the state of Texas

Industry/Entity Type

Building

Requirements
Must have
• Your mockups should include all of the features & content shown in the attached screenshots.

However, you don't have to show all 10 rows of data. You can just do the column headers and one row of data. (It would be repetitive and unnecessary to spend time re-creating the entire grid with all of that data just to show your visual styling.)

The design should reflect the following concepts:

- Texas
- Education
- Simplicity
- Helpfulness
- Trust
- Professionalism

If I select your design, I will want your design source files (Illustrator, Photoshop, etc.)
Nice to have
• A logo in the upper left corner for PLUMB-Finder. The logo should definitely communicate the design concepts described under "must have."

```html
<!DOCTYPE html>
<html lang="en">
<head>
<meta charset="utf-8">
<title>PLUMB-Finder · Student Data</title>
<link href="https://fonts.googleapis.com/css2?family=PT+Sans:wght@400;700&display=swap" rel="stylesheet">
<style>
  :root {
    --page-bg: #efefef;
    --panel-bg: #ffffff;
    --brand: #13aee4;
    --brand-dark: #0a8fc4;
    --banner-deep: #0a8fb0;
    --banner-light: #46d3ea;
    --text: #555555;
    --text-muted: #777777;
    --link: #1a8fc0;
    --row-top: #f2f2f2;
    --row-bottom: #e2e2e2;
    --row-line: #cfcfcf;
    --nav-top: #f4f4f4;
    --nav-bottom: #e4e4e4;
  }
  * { box-sizing: border-box; margin: 0; padding: 0; }
  html, body { width: 1200px; height: 704px; overflow: hidden; }
  body {
    background: var(--page-bg);
    font-family: "PT Sans", Arial, sans-serif;
    color: var(--text);
    font-size: 12px;
    position: relative;
  }
  .app { position: absolute; left: 44px; top: 0; width: 1112px; }

  .banner {
    height: 143px;
    position: relative;
    background:
      radial-gradient(ellipse 60% 120% at 70% 20%, rgba(255,255,255,.35), transparent 60%),
      linear-gradient(100deg, var(--banner-deep) 0%, var(--banner-light) 45%, #1fb7d8 70%, var(--banner-deep) 100%);
  }
  .brand {
    position: absolute; left: 20px; top: 52px;
    display: flex; align-items: center; gap: 10px;
  }
  .brand-dot { width: 18px; height: 18px; border-radius: 50%; background: #ffffff; }
  .brand-name { color: #ffffff; font-weight: 700; font-size: 30px; letter-spacing: .5px; }

  .nav {
    height: 40px; position: relative;
    background: linear-gradient(var(--nav-top), var(--nav-bottom));
    border-bottom: 3px solid var(--brand);
  }
  .tab {
    position: absolute; top: 0; height: 37px; line-height: 37px;
    text-align: center; font-size: 12.5px; color: var(--text-muted);
  }
  .tab-instructions { left: 0; width: 100px; border-right: 1px solid #d4d4d4; }
  .tab-active {
    left: 100px; width: 103px; background: var(--brand); color: #fff;
  }
  .tab-active::after {
    content: ""; position: absolute; left: 46px; bottom: -9px;
    border: 6px solid transparent; border-top-color: var(--brand);
  }
  .user { position: absolute; left: 291px; top: 0; line-height: 37px; font-size: 12.5px; color: #444; }
  .user a { color: var(--link); text-decoration: underline; }
  .user .sep { color: #bbb; margin: 0 5px; }
  .search { position: absolute; left: 588px; top: 7px; display: flex; }
  .search-field {
    width: 145px; height: 24px; border: 1px solid #d6d6d6; border-right: 0;
    background: #fff; border-radius: 3px 0 0 3px; font-size: 11px; color: #999;
    padding: 4px 9px;
  }
  .search-btn { width: 26px; height: 24px; background: var(--brand); border-radius: 0 3px 3px 0; display: flex; align-items: center; justify-content: center; }
  .search-options { position: absolute; left: 776px; top: 0; line-height: 37px; font-size: 11px; color: var(--link); display: flex; align-items: center; gap: 6px; }
  .search-options .arrow { width: 14px; height: 14px; border: 1px solid #ccc; background: #fff; display: flex; align-items: center; justify-content: center; }

  .toolbar {
    margin-top: 14px; height: 30px; background: var(--panel-bg);
    position: relative; font-size: 10.5px; text-transform: uppercase; color: #666;
  }
  .toolbar > div { position: absolute; top: 0; line-height: 30px; }
  .toolbar a { color: var(--link); text-decoration: underline; }
  .tool-count { left: 10px; }
  .tool-count .sep { color: #ccc; margin: 0 10px; }
  .tool-filter { left: 570px; }
  .tool-actions { right: 10px; }
  .tool-actions .sep { color: #ccc; margin: 0 8px; }

  .pager { height: 19px; display: flex; align-items: center; font-size: 10.5px; color: #666; }
  .pager-top { margin-top: 12px; }
  .pager-bottom { margin-top: 5px; }
  .pager .btn {
    height: 19px; line-height: 17px; border: 1px solid #d8d8d8; background: linear-gradient(#f8f8f8,#e6e6e6);
    padding: 0 7px; color: #666; margin-right: -1px;
  }
  .pager .btn-wide { padding: 0 10px; }
  .pager .btn-current { background: var(--brand); color: #fff; border-color: var(--brand); }
  .pager .show { margin-left: 18px; }
  .pager .size { margin: 0 6px; height: 19px; line-height: 17px; border: 1px solid #d8d8d8; background: #fff; padding: 0 7px; }

  .grid { margin-top: 5px; width: 1112px; border-collapse: collapse; table-layout: fixed; }
  .grid th {
    height: 42px; background: linear-gradient(#2fc0ef, var(--brand-dark));
    color: #fff; font-size: 12px; font-weight: 700; text-transform: uppercase;
    border-right: 1px solid rgba(255,255,255,.35);
  }
  .grid td {
    height: 41.6px; text-align: center; font-size: 12px; line-height: 1.15; color: #555;
    background: linear-gradient(var(--row-top), var(--row-bottom));
    border-right: 1px solid var(--row-line); border-bottom: 1px solid #c4c4c4;
  }
  .grid td:last-child, .grid th:last-child { border-right: 0; }
  .grid td:first-child { border-left: 1px solid var(--row-line); }
  .grid td:last-child { border-right: 1px solid var(--row-line); }
</style>
</head>
<body>
<div class="app">
  <header class="banner" role="img" aria-label="Flowing turquoise light-wave backdrop">
    <div class="brand"><span class="brand-dot"></span><span class="brand-name">PLUMB-Finder</span></div>
  </header>

  <nav class="nav">
    <div class="tab tab-instructions">Instructions</div>
    <div class="tab tab-active">Student Data</div>
    <div class="user">Welcome, Dana<span class="sep">|</span><a href="#">my profile</a><span class="sep">|</span><a href="#">log out</a></div>
    <div class="search">
      <div class="search-field">search...</div>
      <div class="search-btn">
        <svg width="12" height="12" viewBox="0 0 12 12"><circle cx="5" cy="5" r="3.5" fill="none" stroke="#fff" stroke-width="1.8"/><line x1="7.6" y1="7.6" x2="11" y2="11" stroke="#fff" stroke-width="2"/></svg>
      </div>
    </div>
    <div class="search-options">Search Options
      <span class="arrow"><svg width="8" height="8" viewBox="0 0 8 8"><path d="M4 1v5M1.5 4L4 6.5 6.5 4" fill="none" stroke="#1a8fc0" stroke-width="1.4"/></svg></span>
    </div>
  </nav>

  <section class="toolbar">
    <div class="tool-count">Showing 36 of 48 columns<span class="sep">|</span><a href="#">Show/hide columns</a></div>
    <div class="tool-filter">3 columns are <a href="#">filtered</a></div>
    <div class="tool-actions"><a href="#">Print</a><span class="sep">|</span><a href="#">Download</a></div>
  </section>

  <div class="pager pager-top">
    <span class="btn btn-wide">Previous</span><span class="btn">1</span><span class="btn btn-current">2</span><span class="btn">3</span><span class="btn">4</span><span class="btn">5</span><span class="btn btn-wide">Next</span>
    <span class="show">Show</span><span class="size">10</span><span>rows per page</span>
  </div>

  <table class="grid">
    <thead>
      <tr><th>Date</th><th>Grade</th><th>ESC</th><th>CDC#</th><th>District</th><th>Campus</th><th>Last Name</th><th>First Name</th><th>MI</th><th>Student ID</th><th>Gender</th><th>DOB</th><th>Hisp</th></tr>
    </thead>
    <tbody>
      <tr><td>411</td><td>9</td><td>10</td><td>9999999901</td><td>Example<br>District</td><td>Example HS</td><td>Accountability</td><td>Marisol</td><td>G</td><td>63054330</td><td>F</td><td>7311996</td><td>1</td></tr>
      <tr><td>411</td><td>9</td><td>10</td><td>9999999901</td><td>Example<br>District</td><td>Example HS</td><td>Accountability</td><td>Marisol</td><td>G</td><td>63054330</td><td>F</td><td>7311996</td><td>1</td></tr>
      <tr><td>411</td><td>9</td><td>10</td><td>9999999901</td><td>Example<br>District</td><td>Example HS</td><td>Accountability</td><td>Marisol</td><td>G</td><td>63054330</td><td>F</td><td>7311996</td><td>1</td></tr>
      <tr><td>411</td><td>9</td><td>10</td><td>9999999901</td><td>Example<br>District</td><td>Example HS</td><td>Accountability</td><td>Marisol</td><td>G</td><td>63054330</td><td>F</td><td>7311996</td><td>1</td></tr>
      <tr><td>411</td><td>9</td><td>10</td><td>9999999901</td><td>Example<br>District</td><td>Example HS</td><td>Accountability</td><td>Marisol</td><td>G</td><td>63054330</td><td>F</td><td>7311996</td><td>1</td></tr>
      <tr><td>411</td><td>9</td><td>10</td><td>9999999901</td><td>Example<br>District</td><td>Example HS</td><td>Accountability</td><td>Marisol</td><td>G</td><td>63054330</td><td>F</td><td>7311996</td><td>1</td></tr>
      <tr><td>411</td><td>9</td><td>10</td><td>9999999901</td><td>Example<br>District</td><td>Example HS</td><td>Accountability</td><td>Marisol</td><td>G</td><td>63054330</td><td>F</td><td>7311996</td><td>1</td></tr>
      <tr><td>411</td><td>9</td><td>10</td><td>9999999901</td><td>Example<br>District</td><td>Example HS</td><td>Accountability</td><td>Marisol</td><td>G</td><td>63054330</td><td>F</td><td>7311996</td><td>1</td></tr>
    </tbody>
  </table>

  <div class="pager pager-bottom">
    <span class="btn btn-wide">Previous</span><span class="btn">1</span><span class="btn btn-current">2</span><span class="btn">3</span><span class="btn">4</span><span class="btn">5</span><span class="btn btn-wide">Next</span>
    <span class="show">Show</span><span class="size">10</span><span>rows per page</span>
  </div>
</div>
</body>
</html>
```